Brick lantern real estate investment company needs a poster design

We would like a poster design size 18 x 24.
Poster wording -
I WANT TO BUY YOUR ( finish with logo) logo uploaded
website- www.bricklantern.example
phone # 555-817-2643 ( color red for the phone number)
we would like to see the poster on 2 different backgrounds
Yellow background
White background
horizontal

```html
<!DOCTYPE html>
<html lang="en">
<head>
<meta charset="utf-8">
<title>Brick lantern – I Want To Buy Your House poster</title>
<link rel="stylesheet" href="https://fonts.googleapis.com/css2?family=Oswald:wght@500&family=Nunito:wght@700;900&family=Arimo:wght@400&display=swap">
<style>
  :root {
    --brand-red: #ff000f;
    --ink-black: #000000;
    --paper-white: #ffffff;
    --call-yellow: #ffed00;
  }
  html, body {
    margin: 0;
    padding: 0;
    width: 1200px;
    height: 900px;
    overflow: hidden;
    background: var(--paper-white);
  }
  .poster {
    display: block;
    width: 1200px;
    height: 900px;
  }
  .band-red { fill: var(--brand-red); }
  .band-black { fill: var(--ink-black); }
  .call-badge { fill: var(--call-yellow); }
  .call-icon { fill: var(--ink-black); }
  .headline {
    font-family: "Oswald", "Arial Narrow", sans-serif;
    font-weight: 500;
    fill: var(--paper-white);
  }
  .brand-name {
    font-family: "Nunito", "Arial", sans-serif;
    font-weight: 900;
    fill: var(--ink-black);
  }
  .website {
    font-family: "Nunito", "Arial", sans-serif;
    font-weight: 700;
    fill: var(--paper-white);
  }
  .phone-number {
    font-family: "Arimo", "Arial", sans-serif;
    font-weight: 400;
    fill: var(--paper-white);
  }
</style>
</head>
<body>
<svg class="poster" viewBox="0 0 1200 900" xmlns="http://www.w3.org/2000/svg">
  <rect class="band-red" x="0" y="0" width="1200" height="900"/>
  <path fill="#ffffff" d="M0,238 C250,130 470,162 600,192 C860,250 1080,250 1200,220 V470 L0,520 Z"/>
  <path class="band-black" d="M0,508 C100,465 200,455 304,455 C520,455 720,494 900,494 C1020,494 1120,478 1200,450 V680 C1100,705 1020,710 960,704 C760,690 620,648 480,648 C300,648 150,700 0,832 Z"/>

  <text class="headline" x="40" y="178" font-size="200" textLength="1128" lengthAdjust="spacingAndGlyphs">I WANT TO BUY YOUR</text>

  <text class="brand-name" x="574" y="420" font-size="150" text-anchor="middle" textLength="1060" lengthAdjust="spacingAndGlyphs">Brick lantern</text>

  <text class="website" x="586" y="608" font-size="112" text-anchor="middle" textLength="1060" lengthAdjust="spacingAndGlyphs">www.bricklantern.example</text>

  <circle class="call-badge" cx="132" cy="766" r="100"/>
  <path class="call-icon" transform="translate(72,704) scale(5)" d="M6.62 10.79c1.44 2.83 3.76 5.14 6.59 6.59l2.2-2.2c.27-.27.67-.36 1.02-.24 1.12.37 2.33.57 3.57.57.55 0 1 .45 1 1V20c0 .55-.45 1-1 1-9.39 0-17-7.61-17-17 0-.55.45-1 1-1h3.5c.55 0 1 .45 1 1 0 1.25.2 2.45.57 3.57.11.35.03.74-.25 1.02l-2.2 2.2z"/>

  <text class="phone-number" x="252" y="852" font-size="168" textLength="908" lengthAdjust="spacingAndGlyphs">555-817-2643</text>
</svg>
</body>
</html>
```